Business Card Design Project : Ferncliff Media

In preparation for market launch, Whistler's Ferncliff Media require the development of a business card. Ferncliff Media is a Community online publishing web portal. We provide the the city of Whistler located in B.C. (Canada) business directories, News, Classified ads, News, Events and blogs etc.

The main focus of the brand is to help local businesses to corporate with their online advertisement and marketing. Meeting our clients face to face is a must (B2B).

Target Market(s)

The target market is B2B customers. Business Owners to Marketing, advertising Managers

Industry/Entity Type

Business

Requirements
Must have
• - The business card will be two sided.
the BACK side will have our logo which consist of (icon, url,slogan) submited. The logo will be middle and centred.

The FRONT side should have company details:

Company Legal Name: TALLPINE FERNCLIFF MEDIA

Dale Morrow
Director of Sales & Marketing

www.tallpineferncliff.biz
dale@tallpineferncliff.biz

Phone: 604 555 0138
#2217 - 581 E. Harlow Ave.
Vancouver, B.C. V6N2K4 Canada
Nice to have
• - For the "FRONT" side of our business card. You can separate or re-arrange with our logo components (icon, logo,slogan). It does not have to be together.

Also our company legal name is rather long so arrange or organize the name in a way to make it shorter. Your experience and creativity will have to come in play.
Should not have
• should not have other colors beside logo color and black text (2 colors). Also nothing Three dimensional

```html
<!DOCTYPE html>
<html lang="en">
<head>
<meta charset="utf-8">
<title>Tallpine Ferncliff Media – Business Cards</title>
<link rel="stylesheet" href="https://fonts.googleapis.com/css2?family=Archivo:wght@400;700;800&family=Open+Sans:wght@400;600&display=swap">
<style>
  :root {
    --brand-blue: #1a80cf;
    --ink-black: #1d1d1d;
    --ink-grey: #4a4a4a;
    --paper-white: #ffffff;
    --backdrop: #2e2e2e;
  }
  * { margin: 0; padding: 0; box-sizing: border-box; }
  html, body {
    width: 1200px;
    height: 748px;
    overflow: hidden;
    background: var(--backdrop);
  }
  .canvas {
    position: relative;
    width: 1200px;
    height: 748px;
  }
  .card {
    position: absolute;
    overflow: hidden;
  }

  /* Back side: logo centred */
  .card-back {
    left: 215px;
    top: 95px;
    width: 440px;
    height: 255px;
    background: var(--paper-white);
    display: flex;
    flex-direction: column;
    align-items: center;
    justify-content: center;
    font-family: "Open Sans", sans-serif;
  }
  .brand-lockup {
    display: flex;
    align-items: center;
    gap: 10px;
  }
  .brand-dot {
    width: 22px;
    height: 22px;
    border-radius: 50%;
    background: var(--brand-blue);
  }
  .brand-url {
    font-size: 20px;
    font-weight: 600;
    color: var(--ink-grey);
    letter-spacing: -0.2px;
  }
  .brand-slogan {
    margin-top: 2px;
    font-size: 15px;
    color: var(--brand-blue);
  }

  /* Front side: company details */
  .card-front {
    left: 485px;
    top: 385px;
    width: 480px;
    height: 270px;
    background: var(--brand-blue);
    font-family: "Archivo", sans-serif;
  }
  .contact {
    position: absolute;
    left: 265px;
    top: 30px;
    z-index: 2;
    color: var(--paper-white);
    font-size: 10.5px;
    line-height: 1.3;
    white-space: nowrap;
  }
  .contact-name {
    font-size: 14px;
    font-weight: 700;
  }
  .contact-title { margin-bottom: 10px; }
  .contact-lines { margin-bottom: 8px; }
  .company-name {
    position: absolute;
    left: 42px;
    bottom: 30px;
    z-index: 2;
    color: var(--ink-black);
    font-size: 25px;
    font-weight: 800;
    line-height: 1.05;
    letter-spacing: 0.5px;
  }
  .corner-mark {
    position: absolute;
    right: -40px;
    bottom: -150px;
    width: 240px;
    height: 240px;
    border-radius: 50%;
    background: var(--ink-black);
  }
</style>
</head>
<body>
<main class="canvas">
  <section class="card card-back" aria-label="Business card back">
    <div class="brand-lockup">
      <span class="brand-dot"></span>
      <span class="brand-url">www.tallpineferncliff.biz</span>
    </div>
    <p class="brand-slogan">Your information gateway</p>
  </section>

  <section class="card card-front" aria-label="Business card front">
    <div class="contact">
      <p class="contact-name">Dale Morrow</p>
      <p class="contact-title">Director of Sales &amp; Marketing</p>
      <div class="contact-lines">
        <p>Phone: 604 555 0138</p>
        <p>www.tallpineferncliff.biz</p>
        <p>dale@tallpineferncliff.biz</p>
      </div>
      <div class="contact-address">
        <p>#2217 - 581 E. Harlow</p>
        <p>Ave. Vancouver, B.C. V6N2K4 Canada</p>
      </div>
    </div>
    <div class="corner-mark"></div>
    <h1 class="company-name">TALLPINE<br>FERNCLIFF<br>MEDIA</h1>
  </section>
</main>
</body>
</html>
```